Summit Grading a Masonry LLC business card

My current business card is very plain. it has my logo and contact information. I woud like something that stands out from the rest. please take a look at my website to see about my company.

Compayt Name - Summit Grading And Masonry
Owner - Martin Galloway
Business Address
Business Website - www.summitgradingandmasonry.example
Email - Summitgradingandmasonry@mailbox.example
Phone - 555-214-3867
Fax - 555-630-2719

Target Market(s)

Everyone age tang is 18 - 85

Industry/Entity Type

Business

Contact Information for Business Card

Nice and professional all in one.

Font styles to use
Serif
Other font styles liked:
• Up to you

Requirements
Must have
• All contact info. The design is up to you.
Nice to have
• All the contact info the design is up to you
Should not have
• I don't have any

```html
<!DOCTYPE html>
<html lang="en">
<head>
<meta charset="utf-8">
<title>Summit Grading &amp; Masonry LLC — Business Card</title>
<link rel="stylesheet" href="https://fonts.googleapis.com/css2?family=Open+Sans:wght@400;600;700&display=swap">
<style>
  :root {
    --backdrop: #e6e3de;
    --card-dark: #2a2b2d;
    --card-light: #f6f6f4;
    --ink-light: #d9d9d9;
    --ink-muted: #9a9a9a;
    --ink-dark: #1c1c1c;
    --accent-bar: #a9a9a9;
    --icon: #8c8c8c;
  }
  * { margin: 0; padding: 0; box-sizing: border-box; }
  html, body {
    width: 1200px; height: 801px; overflow: hidden;
    background: var(--backdrop);
    font-family: "Open Sans", Arial, sans-serif;
  }
  .stage { position: relative; width: 1200px; height: 801px; }
  .card {
    position: absolute; width: 525px; height: 300px;
    border-radius: 3px;
    box-shadow: 0 8px 22px rgba(0,0,0,.18);
  }
  /* Front */
  .card-front {
    left: 580px; top: 60px;
    background: var(--card-dark);
    color: var(--ink-light);
    display: flex; flex-direction: column; align-items: center; justify-content: center;
    text-align: center;
  }
  .front-name {
    font-weight: 700; font-size: 30px; line-height: 1.1;
    letter-spacing: 1px; text-transform: uppercase; color: var(--ink-light);
  }
  .services {
    margin-top: 22px; font-size: 12.5px; color: var(--ink-muted);
  }
  .services span.sep { margin: 0 8px; }
  .website { margin-top: 14px; font-size: 13px; color: var(--ink-muted); }
  /* Back */
  .card-back {
    left: 110px; top: 420px;
    background: var(--card-light);
    color: var(--ink-dark);
  }
  .person { position: absolute; left: 28px; top: 28px; padding-left: 18px; }
  .person::before {
    content: ""; position: absolute; left: 0; top: 2px;
    width: 9px; height: 44px; background: var(--accent-bar);
  }
  .person-name { font-size: 20px; line-height: 1.05; font-weight: 400; }
  .person-name b { font-weight: 700; }
  .person-role { font-size: 17px; line-height: 1.05; color: var(--ink-muted); }
  .back-name {
    position: absolute; right: 30px; top: 118px; width: 210px;
    font-weight: 700; font-size: 17px; line-height: 1.1;
    text-transform: uppercase; text-align: right; color: var(--ink-dark);
  }
  .contacts {
    position: absolute; left: 28px; bottom: 28px; list-style: none;
    font-size: 14px; line-height: 1.55;
  }
  .contacts li { display: flex; align-items: center; gap: 12px; }
  .contacts svg { width: 14px; height: 14px; fill: var(--icon); flex: none; }
</style>
</head>
<body>
<main class="stage">
  <section class="card card-front">
    <h1 class="front-name">Summit Grading<br>&amp; Masonry LLC</h1>
    <p class="services">Asphalt Paving<span class="sep">|</span>Retaining Walls<span class="sep">|</span>Excavation &amp; Grading<span class="sep">|</span>Snow Removal</p>
    <p class="website">www.summitgradingandmasonry.example</p>
  </section>

  <section class="card card-back">
    <div class="person">
      <p class="person-name">Martin <b>Galloway</b></p>
      <p class="person-role">Owner</p>
    </div>
    <p class="back-name">Summit Grading<br>&amp; Masonry LLC</p>
    <ul class="contacts">
      <li><svg viewBox="0 0 16 16"><path d="M8 0a5.5 5.5 0 0 0-5.5 5.5C2.5 10 8 16 8 16s5.5-6 5.5-10.5A5.5 5.5 0 0 0 8 0zm0 8a2.5 2.5 0 1 1 0-5 2.5 2.5 0 0 1 0 5z"/></svg>418 Ridge Ave, Cedar Falls, NY 10000</li>
      <li><svg viewBox="0 0 16 16"><path d="M3.6 1l2.6 3-1.5 2a9 9 0 0 0 5.3 5.3l2-1.5 3 2.6-1.6 2.4C7.6 15 1 8.4 1.2 2.6z"/></svg>(555) 214-3867</li>
      <li><svg viewBox="0 0 16 16"><path d="M4 1h8v4H4zM1 6h14v7h-3v2H4v-2H1zm4 5v3h6v-3z"/></svg>555-630-2719</li>
      <li><svg viewBox="0 0 16 16"><path d="M0 3h16v10H0zm1.5 1.2L8 9l6.5-4.8V3.8L8 8.3 1.5 3.8z"/></svg>summitgradingandmasonry@mailbox.example</li>
    </ul>
  </section>
</main>
</body>
</html>
```